Business Card Design Project

An education/enrichment centre needs a business card for the directors and teachers. Attached is the logo. apart from the logo, the tact line "learning through experience" is needed to be shown in the card

```html
<!DOCTYPE html>
<html lang="en">
<head>
<meta charset="utf-8">
<title>Bright Grove Campus – Business Card</title>
<link rel="stylesheet" href="https://fonts.googleapis.com/css2?family=Open+Sans:wght@400;600&family=Libre+Baskerville&display=swap">
<style>
  :root {
    --stage: #2e2f31;
    --paper: #ffffff;
    --brand-blue: #3a4fa3;
    --band-light: #4d6cc2;
    --band-dark: #3a52a6;
    --back-light: #1f4fa0;
    --back-dark: #253a86;
    --ink-white: #ffffff;
    --ink-dark: #222222;
  }
  * { margin: 0; padding: 0; box-sizing: border-box; }
  html, body { width: 1000px; height: 1200px; overflow: hidden; }
  body { background: var(--stage); position: relative; font-family: "Open Sans", sans-serif; }

  .card { position: absolute; width: 723px; height: 423px; overflow: hidden; box-shadow: 0 4px 14px rgba(0,0,0,.5); }
  .card--front { left: 145px; top: 72px; background: var(--paper); }
  .card--back { left: 139px; top: 637px; background: radial-gradient(circle at 52% 40%, var(--back-light), var(--back-dark) 75%); }

  .front__band { position: absolute; left: 0; top: 254px; width: 100%; height: 169px;
    background: radial-gradient(ellipse at 55% 30%, var(--band-light), var(--band-dark) 70%); }

  .brand-name { position: absolute; left: 0; width: 100%; text-align: center;
    font-family: "Libre Baskerville", serif; letter-spacing: 2px; }
  .card--front .brand-name { top: 150px; font-size: 22px; color: var(--brand-blue); }
  .card--back .brand-name { top: 190px; font-size: 36px; color: var(--ink-white); letter-spacing: 4px; }

  .tagline { position: absolute; left: 262px; width: 200px; top: 278px; text-align: center;
    font-family: "Libre Baskerville", serif; font-size: 15px; line-height: 24px; color: var(--ink-white); }

  .person { position: absolute; right: 34px; top: 190px; text-align: right; }
  .person__name { font-weight: 600; font-size: 21px; color: var(--brand-blue); letter-spacing: .5px; }
  .person__role { font-family: "Libre Baskerville", serif; font-size: 15px; color: var(--ink-dark); margin-top: -2px; }

  .contact { position: absolute; display: flex; align-items: center; gap: 8px;
    font-size: 15px; color: var(--ink-white); }
  .contact svg { flex: none; }
  .contact--mobile { left: 35px; top: 286px; }
  .contact--email { left: 35px; top: 320px; }
  .contact--phone { right: 34px; top: 286px; }
  .contact--web { right: 34px; top: 320px; }
</style>
</head>
<body>

<section class="card card--front" aria-label="Business card front">
  <div class="front__band"></div>
  <div class="brand-name">BRIGHT GROVE CAMPUS</div>
  <div class="tagline">Learning Through<br>Experience</div>

  <div class="person">
    <div class="person__name">ALEX MORGAN</div>
    <div class="person__role">Directors</div>
  </div>

  <div class="contact contact--mobile">
    <svg width="14" height="18" viewBox="0 0 14 18"><rect x="1.5" y="1" width="11" height="16" rx="2" fill="none" stroke="#fff" stroke-width="1.6"/><circle cx="7" cy="14" r="1" fill="#fff"/></svg>
    <span>+1 555 010 2040</span>
  </div>
  <div class="contact contact--email">
    <svg width="18" height="13" viewBox="0 0 18 13"><rect x="0" y="0" width="18" height="13" fill="#fff"/><path d="M0 0 L9 7 L18 0" fill="none" stroke="#3a52a6" stroke-width="1.4"/></svg>
    <span>info@brightgrovecampus.com</span>
  </div>
  <div class="contact contact--phone">
    <span>+1 555 010 2040</span>
    <svg width="16" height="16" viewBox="0 0 16 16"><path d="M3 1 L6 1 L7 5 L5 6.5 C6 9 7.5 10.5 9.5 11.5 L11 9.5 L15 10.5 L15 13.5 C15 14.5 14 15 13 15 C6.5 14.5 1.5 9.5 1 3 C1 2 2 1 3 1 Z" fill="#fff"/></svg>
  </div>
  <div class="contact contact--web">
    <span>www.brightgrovecampus.com</span>
    <svg width="16" height="16" viewBox="0 0 16 16"><circle cx="8" cy="8" r="6.8" fill="none" stroke="#fff" stroke-width="1.6"/></svg>
  </div>
</section>

<section class="card card--back" aria-label="Business card back">
  <div class="brand-name">BRIGHT GROVE CAMPUS</div>
</section>

</body>
</html>
```